Paths to Delight E-card design - Potential for other work

I am looking for a designer to create e card, thank you design templates for my new not for profit website www.pathstodelight.com.au.

They will have simple imagery, with a subtle and soft illustration which reflects some sort of emotion. Think of patterns and textures.

The main focus of the card will be the text submitted as the "Path to Delight". For an example of the text please see http://www.pathstodelight.com.au/search-for-ideas/.

The width of the card / image (which will be displayed on a web page) will be 700px max, and there is no restriction on height.

The colours will be similar to the website colours although possibly softer/pastal colours.

The design should contain a header/title "You've amazed me, thank you" before the actual words merged from the site as the Path to Delight. It will appear on a blank page on the website with the same header so it doesn't have to be similar to the website design.

I will upload similar designs I like to make your job easier on Monday.

Although this job is only for a couple of simple designs, I will require more in the future so there is potential for ongoing work. I am therefore looking for a provider who is reliable, trustworthy, efficient and of course has a creative design flair.

If you want to be a part of a great cause, please submit your designs. I look forward to working with you.

Thank you.

Target Market(s)

Everyone with a kind heart ;0)

Industry/Entity Type

Work

Requirements
Nice to have
• In terms of the attached files, 1 and 2 give an example of a pattern that is quite nice. Number 4 shows the colours I quite like with the orange. We want the e card to evoke emotion. (please note the design Is for an e card, not business card. This is just an example of a design, please ignore the fact it is on a business card.
Should not have
• Too much going on

```html
<!DOCTYPE html>
<html lang="en">
<head>
<meta charset="utf-8">
<title>Paths to Delight – Thank You E-card</title>
<link rel="stylesheet" href="https://fonts.googleapis.com/css2?family=Cormorant+Garamond:ital,wght@1,600&family=Questrial&display=swap">
<style>
  :root {
    --backdrop: #e4e4e4;
    --card-orange: #f06023;
    --ink-white: #ffffff;
    --text-shadow: rgba(90, 30, 5, 0.55);
    --ornament-light: rgba(255, 240, 232, 0.8);
    --ornament-peach: rgba(246, 178, 146, 0.6);
    --ornament-fade: rgba(240, 96, 35, 0);
  }
  * { margin: 0; padding: 0; box-sizing: border-box; }
  html, body {
    width: 1200px;
    height: 900px;
    overflow: hidden;
    background: var(--backdrop);
  }
  .ecard {
    position: absolute;
    left: 97px;
    top: 126px;
    width: 1003px;
    height: 648px;
    background: var(--card-orange);
    overflow: hidden;
  }
  .ecard__headline {
    position: absolute;
    inset: 0;
    font-family: "Cormorant Garamond", "Times New Roman", serif;
    font-style: italic;
    font-weight: 600;
    font-size: 80px;
    letter-spacing: 2px;
    line-height: 1;
    color: var(--ink-white);
    text-shadow: 2px 3px 3px var(--text-shadow);
    white-space: nowrap;
  }
  .ecard__headline-line { position: absolute; display: block; }
  .ecard__headline-line--first { left: 66px; top: 189px; }
  .ecard__headline-line--second { left: 343px; top: 287px; }
  .ecard__url {
    position: absolute;
    left: 275px;
    top: 549px;
    font-family: "Questrial", "Century Gothic", sans-serif;
    font-size: 32px;
    letter-spacing: 1.5px;
    color: var(--ink-white);
    white-space: nowrap;
  }
  .ecard__ornament {
    position: absolute;
    left: 640px;
    top: 90px;
    width: 380px;
    height: 570px;
    background:
      radial-gradient(ellipse 45% 40% at 62% 66%, var(--ornament-light) 0%, var(--ornament-peach) 50%, var(--ornament-fade) 100%),
      radial-gradient(ellipse 40% 35% at 45% 30%, var(--ornament-peach) 0%, var(--ornament-fade) 100%);
  }
</style>
</head>
<body>
  <main class="ecard">
    <div class="ecard__ornament" role="img" aria-label="Soft flourish of swirling black, white and peach scrollwork in the lower right corner"></div>
    <h1 class="ecard__headline">
      <span class="ecard__headline-line ecard__headline-line--first">You've amazed me,</span>
      <span class="ecard__headline-line ecard__headline-line--second">thank you</span>
    </h1>
    <p class="ecard__url">www.pathstodelight.com.au</p>
  </main>
</body>
</html>
```